Football and Sports Management Agency Stationary

We have a logo, fonts, website and colour palette.
We need the logo refined by a proper designer and then business stationary designed. You can see on the website how it needs adjusting by a designers eye.
The company is a high end sports management company aiming to attract and represent professional athletes. The name Velorin is to indicate a 'Constellation of Stars' ie our clients. The dots on the star should be slightly different sizes to reflect that some clients will be bigger than others.
Colours:
#e6e6e6
#edd2a4
#caaa72 (main gold and also used on site)
#3f3f42
#001d38
#edeced (on website)
#191c23 (on website)
Font:
QT (velorin)
QT Melbrook (sports management)
We would like:
- Letterhead (word and indesign and PDF print format). I have attached an example for one I like. It's quiet a clean design with the contact details and address taking up only a small amount of room.
- Business card (dark on the back with the logo, personal details on the front). Only needs name, title, email, website and phone number. No company address (in PDF and indesign format)
- Powerpoint slide theme
- Logo in vector format for light and dark versions and single colour versions. And optimised web version
- Simple brand guide PDF showing colour, font and logo (a one/two page PDF)
Any questions, please ask.
NEW INFO:
Contact Details
Maren Solwick
Director
Mobile: +44 7630 218 977
Phone: +44 0113 872 604
Email: maren@velorinathletic.example
Web: velorinathletic.example
Corran Lodge, 14 Mill Bank Road, Stockport, SK4 9TW
Company number 40718362
Target Market(s)
Professional athletes, professional sports teams.
Industry/Entity Type
Management
Requirements
Must have
- NEW
- The designs must look cool, classy and high quality. My suggestion for this is to keep the text small and precise with uncomplicated design.
Nice to have
- Application of brand displayed on stationary and additional pieces of stationary branded.
- Draw some inspiration from the website. eg the slant angles used separate the sections.
Should not have
- Don't create new logos etc.

```html
<!DOCTYPE html>
<html lang="en">
<head>
<meta charset="utf-8">
<title>Velorin Stationery</title>
<link rel="stylesheet" href="https://fonts.googleapis.com/css2?family=Work+Sans:wght@300;400;500&display=swap">
<style>
  :root {
    --canvas: #ebebeb;
    --paper: #ffffff;
    --charcoal: #3f3f42;
    --ink: #2b2b2d;
    --gold: #caaa72;
    --body-grey: #9a9a9a;
    --rule: #4a4a4d;
    --sig-fill: #ececec;
  }
  * { box-sizing: border-box; margin: 0; padding: 0; }
  html, body { width: 1200px; height: 807px; overflow: hidden; }
  body {
    position: relative;
    background: var(--canvas);
    font-family: "Work Sans", Arial, sans-serif;
    color: var(--ink);
  }
  .sheet {
    position: absolute;
    background: var(--paper);
    box-shadow: 0 3px 10px rgba(0,0,0,0.18);
  }

  /* Wordmark */
  .wordmark {
    position: absolute;
    display: flex;
    align-items: center;
    gap: 10px;
    font-weight: 300;
    letter-spacing: 0.48em;
    color: var(--charcoal);
    white-space: nowrap;
  }
  .wordmark .dot {
    width: 7px; height: 7px;
    border-radius: 50%;
    background: var(--gold);
    flex: none;
  }
  .wordmark.on-dark { color: #ffffff; }

  .divider {
    position: absolute;
    width: 1.5px;
    background: var(--rule);
  }

  /* Contact block */
  .contact {
    position: absolute;
    font-size: 8.8px;
    line-height: 1.25;
    color: var(--ink);
    font-weight: 400;
  }
  .contact .address { margin-bottom: 6px; }
  .contact .line { display: flex; align-items: center; gap: 5px; }
  .contact .icon { width: 6px; height: 6px; flex: none; }
  .contact .accent { color: var(--gold); }

  /* Letterhead */
  .letterhead { left: 54px; top: 42px; width: 508px; height: 720px; }
  .letterhead .wordmark { left: 36px; top: 66px; font-size: 18px; }
  .letterhead .divider { left: 282px; top: 47px; height: 58px; }
  .letterhead .contact { left: 359px; top: 46px; }
  .salutation {
    position: absolute; left: 36px; top: 228px;
    font-size: 14px; color: #8a8a8a; font-weight: 400;
  }
  .letter-body {
    position: absolute; left: 36px; top: 276px; width: 440px;
    font-size: 8.7px; line-height: 13.2px; color: var(--body-grey);
  }
  .letter-body p { margin-bottom: 15px; }
  .signature {
    position: absolute; left: 36px; top: 580px; width: 126px; height: 28px;
    background: var(--sig-fill); border-radius: 3px;
  }

  /* Business cards */
  .card-front { left: 631px; top: 43px; width: 245px; height: 139px; }
  .card-front .wordmark { left: 17px; top: 61px; font-size: 11px; gap: 7px; }
  .card-front .wordmark .dot { width: 5px; height: 5px; }
  .card-front .divider { left: 133px; top: 38px; height: 64px; width: 1px; }
  .card-front .person { position: absolute; left: 145px; top: 36px; }
  .card-front .name { font-size: 9.5px; color: var(--gold); font-weight: 400; letter-spacing: 0.02em; }
  .card-front .title { font-size: 6px; margin-top: 2px; margin-bottom: 5px; }
  .card-front .details { font-size: 5.6px; line-height: 1.3; }
  .card-front .details .address { margin-bottom: 4px; }
  .card-front .details .line { display: flex; align-items: center; gap: 3px; }
  .card-front .details .icon { width: 4px; height: 4px; }
  .card-front .details .accent { color: var(--gold); }

  .card-back { left: 890px; top: 43px; width: 245px; height: 139px; background: var(--charcoal); }
  .card-back .wordmark { left: 53px; top: 61px; font-size: 14px; }

  /* Envelopes */
  .envelope-back { left: 631px; top: 222px; width: 503px; height: 252px; }
  .envelope-back .flap { position: absolute; left: 0; top: 0; width: 503px; height: 76px; }
  .envelope-back .wordmark { left: 184px; top: 29px; font-size: 14px; }

  .envelope-front { left: 631px; top: 512px; width: 503px; height: 251px; }
  .envelope-front .wordmark { left: 17px; top: 193px; font-size: 17px; }
  .envelope-front .divider { left: 204px; top: 178px; height: 56px; }
  .envelope-front .contact { left: 231px; top: 175px; }
</style>
</head>
<body>

  <!-- Letterhead -->
  <section class="sheet letterhead" aria-label="Letterhead">
    <div class="wordmark"><span class="dot"></span>VELORIN</div>
    <div class="divider"></div>
    <div class="contact">
      <div class="address">P.O. Box 508362,<br>Harlow Creek, Texas 75990</div>
      <div class="line"><svg class="icon" viewBox="0 0 10 10"><path d="M2 1 L4 1 L5 3.5 L3.8 4.5 Q4.8 6.3 6 6.6 L7 5.4 L9 6.4 L9 8.5 Q5 9.5 1.5 5 Q0.8 2.5 2 1Z" fill="#caaa72"/></svg>214.555.0187</div>
      <div class="line"><svg class="icon" viewBox="0 0 10 10"><rect x="1" y="2.5" width="8" height="5.5" fill="none" stroke="#caaa72" stroke-width="1.2"/><path d="M1 2.5 L5 6 L9 2.5" fill="none" stroke="#caaa72" stroke-width="1.2"/></svg>info@velorinathletic.example</div>
      <div class="line"><svg class="icon" viewBox="0 0 10 10"><circle cx="5" cy="5" r="4" fill="#caaa72"/></svg><span>www.<span class="accent">velorinathletic</span>.example</span></div>
    </div>

    <p class="salutation">Dear sir,</p>
    <div class="letter-body">
      <p>Lorem ipsum dolor sit amet, an vel recteque dissentiet, detracto albucius platonem ex vel, eros repudiandae cu. Atqui aliquando nec an, unum graece adolescens vel ad. Id odio scae has, iudico euismod atomorum ius ea, cum ea honestatis quaerendum theophrastus. Mea honestatis quaerendum theophrastus. Mea</p>
      <p>Lorem ipsum dolor sit amet, an vel recteque dissentiet, detracto albucius platonem ex vel, eros repudiandae cu. Atqui aliquando nec an, unum graece adolescens vel ad. Id odio scae has, iudico euismod atomorum ius ea, cum ea honestatis quaerendum theophrastus. Mea doming repudiandae ex, cu cum civibus assentior posidonium. Quo etiam pertinax ex, te eros repudiandae cu. Atqui aliquando nec an, unum graece adolescens vel ad. Id odio scae honestatis quaerendum theophrastus. Mea</p>
      <p>Lorem ipsum dolor sit amet, an vel recteque dissentiet, detracto albucius platonem ex vel, eros repudiandae cu. Atqui aliquando nec an, unum graece adolescens vel ad. Id odio scae has, iudico euismod atomorum ius ea, cum ea honestatis quaerendum theophrastus. Mea honestatis quaerendum theophrastus. Mea</p>
      <p>eros repudiandae cu. Atqui aliquando nec an, unum graece adolescens vel ad. Id odio scae honestatis quaerendum theophrastus. Mea posidonium. Quo etiam pertinax ex, te etiam pertinax ex, te</p>
    </div>
    <div class="signature" role="img" aria-label="Handwritten signature of Tobin Ashcroft"></div>
  </section>

  <!-- Business card front -->
  <section class="sheet card-front" aria-label="Business card front">
    <div class="wordmark"><span class="dot"></span>VELORIN</div>
    <div class="divider"></div>
    <div class="person">
      <div class="name">TOBIN ASHCROFT</div>
      <div class="title">Director</div>
      <div class="details">
        <div class="address">P.O. Box 508362,<br>Harlow Creek, Texas 75990</div>
        <div class="line"><svg class="icon" viewBox="0 0 10 10"><circle cx="5" cy="5" r="4" fill="#caaa72"/></svg>214.555.0187</div>
        <div class="line"><svg class="icon" viewBox="0 0 10 10"><circle cx="5" cy="5" r="4" fill="#caaa72"/></svg>info@velorinathletic.example</div>
        <div class="line"><svg class="icon" viewBox="0 0 10 10"><circle cx="5" cy="5" r="4" fill="#caaa72"/></svg><span>www.<span class="accent">velorinathletic</span>.example</span></div>
      </div>
    </div>
  </section>

  <!-- Business card back -->
  <section class="sheet card-back" aria-label="Business card back">
    <div class="wordmark on-dark"><span class="dot"></span>VELORIN</div>
  </section>

  <!-- Envelope back -->
  <section class="sheet envelope-back" aria-label="Envelope back">
    <svg class="flap" viewBox="0 0 503 76" preserveAspectRatio="none">
      <path d="M0 0 H503 L494 50 Q490 76 462 76 H40 Q14 76 10 50 Z" fill="#3f3f42"/>
    </svg>
    <div class="wordmark on-dark"><span class="dot"></span>VELORIN</div>
  </section>

  <!-- Envelope front -->
  <section class="sheet envelope-front" aria-label="Envelope front">
    <div class="wordmark"><span class="dot"></span>VELORIN</div>
    <div class="divider"></div>
    <div class="contact">
      <div class="address">P.O. Box 508362,<br>Harlow Creek, Texas 75990</div>
      <div class="line"><svg class="icon" viewBox="0 0 10 10"><path d="M2 1 L4 1 L5 3.5 L3.8 4.5 Q4.8 6.3 6 6.6 L7 5.4 L9 6.4 L9 8.5 Q5 9.5 1.5 5 Q0.8 2.5 2 1Z" fill="#caaa72"/></svg>214.555.0187</div>
      <div class="line"><svg class="icon" viewBox="0 0 10 10"><rect x="1" y="2.5" width="8" height="5.5" fill="none" stroke="#caaa72" stroke-width="1.2"/><path d="M1 2.5 L5 6 L9 2.5" fill="none" stroke="#caaa72" stroke-width="1.2"/></svg>info@velorinathletic.example</div>
      <div class="line"><svg class="icon" viewBox="0 0 10 10"><circle cx="5" cy="5" r="4" fill="#caaa72"/></svg><span>www.<span class="accent">velorinathletic</span>.example</span></div>
    </div>
  </section>

</body>
</html>
```